Design a Website Mockup for new furniture center in Thailand

We need to build a webpage for our new designer furniture center; https://www.facebook.com/velmorahomewaresonline?ref=hl. The name of the site will be www.kivrant.com

Please submit your bid for both the design and the coding. We will submit all text and pictures to you. We prefer WORDPRESS.

Thank you,

Torvald

```html
<!DOCTYPE html>
<html lang="en">
<head>
<meta charset="utf-8">
<title>Kivrant Design Furniture</title>
<link href="https://fonts.googleapis.com/css2?family=Questrial&family=Raleway:wght@300;400;600&family=Comfortaa:wght@400&family=Arimo:wght@400;700&display=swap" rel="stylesheet">
<style>
:root{
  --yellow:#f4b820;
  --brown:#4e3a34;
  --ink:#3a3a3a;
  --muted:#8a8a8a;
  --card:#efefef;
  --footer:#2f2f2f;
  --footer-text:#b5b5b5;
  --base:#d4d4d4;
  --paper:#ffffff;
}
*{margin:0;padding:0;box-sizing:border-box}
html,body{width:925px;height:1200px;overflow:hidden;background:var(--paper)}
body{position:relative;font-family:'Arimo',Arial,sans-serif;color:var(--ink)}
.abs{position:absolute}

/* header */
.site-header{left:0;top:0;width:925px;height:80px;background:#fafafa;border-top:3px solid #555}
.site-header::after{content:"";position:absolute;left:0;bottom:-3px;width:925px;height:3px;background:var(--yellow)}
.brand{left:161px;top:14px;font-family:'Questrial',sans-serif;color:var(--brown)}
.brand-name{font-size:38px;letter-spacing:2px;line-height:40px}
.brand-tag{font-size:9.5px;letter-spacing:2.6px;margin-top:2px}
.welcome{left:583px;top:19px;font-size:9px;color:var(--muted)}
.social-top{left:681px;top:13px;display:flex;gap:4px}
.social-top span{width:21px;height:21px;border-radius:50%;background:#d8d8d8;display:block}
.main-nav{left:383px;top:42px;display:flex;height:36px;font-size:10.5px;color:var(--brown)}
.main-nav a{padding:0 13px;line-height:36px;text-decoration:none;color:inherit;border-right:1px solid #e4e4e4}
.main-nav a:last-child{border-right:none}
.main-nav .active{background:var(--yellow);color:#fff;padding:0 13px 0 11px;display:flex;align-items:center;gap:6px}

/* hero */
.hero{left:0;top:83px;width:925px;height:355px;background:linear-gradient(100deg,#5a3b28 0%,#c9b9a6 28%,#6e4630 50%,#8b6a52 70%,#3e2a20 100%)}
.hero-arrow{top:158px;width:34px;height:41px;background:rgba(244,184,32,.85);display:flex;align-items:center;justify-content:center}
.hero-caption{left:188px;top:210px;width:444px;height:100px;background:rgba(60,55,55,.62);padding:8px 22px;color:#fff}
.hero-caption h1{font-family:'Raleway',sans-serif;font-weight:300;font-size:26px;line-height:28px;letter-spacing:.5px}
.hero-caption h1 .big{font-size:33px;line-height:34px;display:block}
.hero-caption p{font-size:8.5px;line-height:12px;margin-top:3px;color:#eee}

/* intro */
.intro{left:161px;top:449px;width:612px;height:22px;display:flex;align-items:center;justify-content:center}
.intro::before{content:"";position:absolute;left:0;right:0;top:10px;height:3px;background:#ececec}
.intro h2{position:relative;background:#fff;padding:0 8px;font-family:'Raleway',sans-serif;font-weight:400;font-size:15px;color:var(--brown)}
.intro h2 em{font-style:normal;color:var(--yellow)}

/* rooms */
.room{top:489px;width:144px;height:221px;background:var(--card)}
.room h3{height:30px;background:var(--brown);color:#fff;font-family:'Raleway',sans-serif;font-weight:400;font-size:12.5px;text-align:center;line-height:32px}
.room-photo{height:90px}
.room p{font-size:8px;line-height:10.5px;color:#666;padding:7px 9px 0}
.btn{display:block;width:56px;height:23px;margin:10px auto 0;background:var(--yellow);color:#fff;font-size:7.5px;line-height:23px;text-align:center}

/* about */
.section-title{font-family:'Raleway',sans-serif;font-weight:400;font-size:14.5px;color:var(--brown)}
.body-copy{font-size:8px;line-height:10.5px;color:#8e8e8e}
.underline{height:4px;background:#ececec;width:204px}
.lead{font-size:11px;line-height:14px;color:#777;font-weight:700}
.testimonial-nav{left:163px;top:923px;width:190px;display:flex;justify-content:space-between;align-items:center;font-size:8.5px;font-weight:700;color:#333}
.sofa{left:472px;top:843px;width:300px;height:99px;background:linear-gradient(180deg,#f2f2f0 0%,#e6e4e0 55%,#8a8784 72%,#d8d4cf 100%)}

/* band */
.band{left:0;top:968px;width:925px;height:45px;background:var(--yellow)}
.tagline{left:159px;top:976px;font-family:'Comfortaa',sans-serif;font-size:21px;color:var(--brown)}
.subscribe{left:516px;top:975px;display:flex;height:27px}
.subscribe .field{width:194px;background:#fff6dc;font-size:8px;color:#999;line-height:27px;padding-left:9px}
.subscribe .go{width:62px;background:#2c2c2c;color:#fff;font-size:8.5px;line-height:27px;text-align:center}

/* footer */
.footer{left:0;top:1013px;width:925px;height:156px;background:var(--footer)}
.foot-title{font-family:'Raleway',sans-serif;font-size:10.5px;color:#ddd}
.foot-list{font-size:8px;line-height:12.5px;color:var(--footer-text);list-style:none}
.foot-social{left:477px;top:1058px;display:flex;gap:3px}
.foot-social span{width:25px;height:25px;background:#6a6a6a;display:block}
.foot-brand{left:657px;top:1037px;font-family:'Questrial',sans-serif;color:var(--yellow)}
.foot-brand .brand-name{font-size:34px;line-height:36px;letter-spacing:2px}
.foot-brand .brand-tag{font-size:9px;letter-spacing:3px;color:var(--yellow)}
.baseline{left:0;top:1169px;width:925px;height:31px;background:var(--base)}
.copyright{left:159px;top:1175px;font-size:7px;color:#555}
</style>
</head>
<body>

<header class="abs site-header">
  <div class="abs brand" style="left:161px;top:11px">
    <div class="brand-name">KIVRANT</div>
    <div class="brand-tag">DESIGN FURNITURE</div>
  </div>
  <div class="abs welcome">Welcome to Kivrant!</div>
  <div class="abs social-top"><span></span><span></span><span></span><span></span></div>
  <nav class="abs main-nav">
    <a class="active" href="#"><svg width="12" height="11" viewBox="0 0 12 11"><path d="M6 0 0 5h1.6v6h3V7.5h2.8V11h3V5H12z" fill="#fff"/></svg>HOME</a>
    <a href="#">ABOUT US</a><a href="#">SERVICES</a><a href="#">PROJECTS</a><a href="#">BLOG</a><a href="#">CONTACTS</a>
  </nav>
</header>

<section class="abs hero" role="img" aria-label="Photo of a modern kitchen with dark wood cabinets and a curved island">
  <div class="abs hero-arrow" style="left:122px"><svg width="8" height="14"><path d="M7 1 1 7l6 6" stroke="#fff" fill="none" stroke-width="1.3"/></svg></div>
  <div class="abs hero-arrow" style="left:777px"><svg width="8" height="14"><path d="M1 1l6 6-6 6" stroke="#fff" fill="none" stroke-width="1.3"/></svg></div>
  <div class="abs hero-caption">
    <h1>UNIQUE AND AFFORDABLE ITEMS <span class="big">FOR YOUR HOME!</span></h1>
    <p>Lorem ipsum dolor consectetur scing elit. Phasellus eu placerat justo. Nam vestibulum imperdiet suscipit....</p>
  </div>
</section>

<div class="abs intro"><h2><em>THINK OF US</em> AS YOUR PERSONAL DESIGN ASSISTANT!</h2></div>

<article class="abs room" style="left:161px"><h3>BEDROOMS</h3><div class="room-photo" role="img" aria-label="Bright bedroom with a white bed" style="background:linear-gradient(180deg,#b9a58c,#e9e4dc 60%,#d6cfc4)"></div><p>Lorem ipsum dolor consectetur scing elit. Phasellus eu placerat justo. Nam vestibulum imperdiet suscipit ac tristique libero porta.</p><span class="btn">Read More</span></article>
<article class="abs room" style="left:317px"><h3>LIVING ROOMS</h3><div class="room-photo" role="img" aria-label="Open living room with wooden shelving" style="background:linear-gradient(180deg,#6b4f3a,#c9b49a 55%,#ece7e0)"></div><p>Lorem ipsum dolor consectetur scing elit. Phasellus eu placerat justo. Nam vestibulum imperdiet suscipit ac tristique libero porta.</p><span class="btn">Read More</span></article>
<article class="abs room" style="left:472px"><h3>KITCHEN ROOMS</h3><div class="room-photo" role="img" aria-label="White modern kitchen with bar stools" style="background:linear-gradient(180deg,#5c5c5c,#c7c7c7 50%,#eeeeee)"></div><p>Lorem ipsum dolor consectetur scing elit. Phasellus eu placerat justo. Nam vestibulum imperdiet suscipit ac tristique libero porta.</p><span class="btn">Read More</span></article>
<article class="abs room" style="left:628px"><h3>DINING ROOMS</h3><div class="room-photo" role="img" aria-label="Dining room with a dark wood table and chairs" style="background:linear-gradient(180deg,#d9cbb8,#6a4630 55%,#3d2a1e)"></div><p>Lorem ipsum dolor consectetur scing elit. Phasellus eu placerat justo. Nam vestibulum imperdiet suscipit ac tristique libero porta.</p><span class="btn">Read More</span></article>

<h2 class="abs section-title" style="left:163px;top:729px">ABOUT US</h2>
<p class="abs body-copy" style="left:163px;top:755px;width:290px">Lorem ipsum dolor consectetur scing elit. Phasellus eu placerat justo. Nam vestibulum imperdiet suscipit ac tristique libero porta. Donec id ante magna. Nullam sollicitudin, ipsum vel hendrerit aliquam, nisi sapien pellentesque odio, sed tincidunt nibh turpis at purus. Ut id magna mauris. Sed luctus rhoncus nisi, id luctus dui fermentum ac. In ac odio eu leo</p>
<h2 class="abs section-title" style="left:163px;top:818px">CLIENT TESTIMONIALS</h2>
<div class="abs underline" style="left:163px;top:843px"></div>
<p class="abs body-copy" style="left:163px;top:863px;width:290px">Lorem ipsum dolor consectetur scing elit. Phasellus eu placerat justo. Nam vestibulum imperdiet suscipit ac tristique libero porta. Donec id ante magna. Nullam sollicitudin, ipsum vel hendrerit aliquam, nisi sapien pellentesque odio, sed tincidunt nibh turpis at purus. Ut id magna mauris. Sed luctus rhoncus nisi, id luctus dui fermentum ac. In ac odio eu leo</p>
<div class="abs testimonial-nav">
  <svg width="8" height="14"><path d="M7 1 1 7l6 6" stroke="#bbb" fill="none" stroke-width="1.5"/></svg>
  <span>Dana Morrow, New York</span>
  <svg width="8" height="14"><path d="M1 1l6 6-6 6" stroke="#bbb" fill="none" stroke-width="1.5"/></svg>
</div>

<h2 class="abs section-title" style="left:472px;top:729px">HOW WE WORK?</h2>
<p class="abs lead" style="left:472px;top:753px;width:300px">Lorem ipsum dolor sit amet, consectetur adipising elit, sed do eiusmod tempor incididunt ut laborede et dolore magna aliqua.</p>
<p class="abs body-copy" style="left:472px;top:803px;width:300px">Lorem ipsum dolor consectetur scing elit. Phasellus eu placerat justo. Nam vestibulum imperdiet suscipit ac tristique libero porta.</p>
<div class="abs sofa" role="img" aria-label="Grey sofa with cushions, coffee table and potted plant"></div>

<div class="abs band"></div>
<div class="abs tagline">style, comfort, quality, selection!</div>
<div class="abs subscribe"><div class="field">Enter your email adress...</div><div class="go">SUBSCRIBE</div></div>

<footer class="abs footer"></footer>
<h4 class="abs foot-title" style="left:161px;top:1040px">QUICK LINKS</h4>
<ul class="abs foot-list" style="left:161px;top:1062px"><li>Home</li><li>About Us</li><li>Products</li><li>Finishing Touches</li><li>Gallery</li><li>Testimonials</li></ul>
<h4 class="abs foot-title" style="left:293px;top:1040px">CONTACT US</h4>
<ul class="abs foot-list" style="left:293px;top:1073px;line-height:15px"><li>UK Telephone: +44 (0)800 000 4 210</li><li>US Telephone: +1 800-555-0142</li></ul>
<h4 class="abs foot-title" style="left:477px;top:1039px;font-size:8px">FOLLOW OUR UPDATES</h4>
<div class="abs foot-social"><span></span><span></span><span></span><span></span></div>
<p class="abs foot-list" style="left:477px;top:1091px;width:150px;font-size:6.5px;line-height:8.5px">Wanna know about our plans? Have some feedback or just want to say hello? Know more about our team and our plans.</p>
<div class="abs foot-brand"><div class="brand-name">KIVRANT</div><div class="brand-tag">DESIGN FURNITURE</div></div>

<div class="abs baseline"></div>
<div class="abs copyright">© 2013 kivrant. All rights reserved</div>

</body>
</html>
```